Graphic design for "How It Works" for VelmoraStyles.com*

VelmoraStyles.com website is for selling custom designer outfits for women and girls in all countries, customers can choose existing designs on this website and customize to their measurements. Customers can also provide their own designs and measurements and our expert designers and tailors get the outfit stitched and delivered to the customer.

We wanted to explain how this entire process works in 4 steps in the form of graphic design with little heading and text describing each step.

Step 1: Select Dress
Its time to choose the beauty you want to adorn yourself with. We have a wide collection of premium dresses, colours and accessories. There is something for everyone! All you need to do is pick. If you can’t find what you are looking for then you can share a picture of what you want, we will get it done whatever you want.

Step 2: Customization
Everyone is different; hence we realise the need for customization of the design and size. Here you select exactly how you want your dress to be. From sleeves to cuts, everything will be done as per your wish. Enter your measurements, lo and behold! You’re done. Leave your comments for even more customization.

Step 3: Designer Consultation
We as a user-friendly brand, aspire to provide the best of services to our clients. Our expert lady designers will help you for everything right from selecting of fabric to design of dress to necessary accessories. Our designers are just a call away!

Step 4: Stitch and Deliver
After you have placed your order, we confirm and verify the details. The boutique completes your order, sends it to us and we deliver it to your doorstep. We also have a team of designers in-house to cater to your premium dressing needs.

```html
<!DOCTYPE html>
<html lang="en">
<head>
<meta charset="utf-8">
<title>How It Works – VelmoraStyles.com</title>
<link rel="stylesheet" href="https://fonts.googleapis.com/css2?family=Fira+Sans+Condensed:wght@600;700&family=Source+Sans+3:wght@400;600;700;800&display=swap">
<style>
  :root{
    --magenta:#c84a82;
    --step-pink:#c4437e;
    --ink:#111111;
    --body:#1c1c1c;
    --white:#ffffff;
    --band-purple:#4b4f9f;
    --band-blue:#1c9fc7;
    --band-sea:#27b08b;
    --band-lime:#84c440;
    --ring-grey:#e4e4e6;
    --scene-soft:#e7e4f2;
  }
  *{margin:0;padding:0;box-sizing:border-box}
  html,body{width:1200px;height:1062px;overflow:hidden;background:var(--white)}
  .sheet{position:relative;width:1200px;height:1062px;overflow:hidden;font-family:"Source Sans 3",sans-serif}
  .backdrop{position:absolute;inset:0}
  .title{
    position:absolute;left:0;top:46px;width:938px;
    display:flex;align-items:center;justify-content:center;gap:16px;
    font-family:"Source Sans 3",sans-serif;font-weight:800;font-size:58px;
    letter-spacing:0.5px;color:var(--ink);line-height:1;
  }
  .title::before,.title::after{content:"";width:110px;height:4px;background:var(--magenta)}
  .step{position:absolute;width:240px;transform:translateX(-50%);text-align:center}
  .step-label{
    font-family:"Fira Sans Condensed",sans-serif;font-weight:700;color:var(--ink);
    font-size:21px;line-height:1;display:flex;align-items:baseline;justify-content:center;gap:6px;
  }
  .step-label .num{font-size:48px;color:var(--step-pink);font-weight:600}
  .step-text{margin-top:10px;font-size:14px;line-height:21.5px;color:var(--body)}
  .step-1{left:187px;top:624px}
  .step-2{left:420px;top:134px}
  .step-3{left:662px;top:624px}
  .step-4{left:890px;top:134px}
  .band-label{font-family:"Source Sans 3",sans-serif;font-weight:700;font-size:21px;fill:var(--white);letter-spacing:0.4px}
  .web-address{
    position:absolute;right:27px;top:986px;color:var(--white);
    font-family:"Source Sans 3",sans-serif;font-weight:600;font-size:34px;letter-spacing:0.3px;
  }
</style>
</head>
<body>
<main class="sheet">
  <svg class="backdrop" width="1200" height="1062" viewBox="0 0 1200 1062" aria-hidden="false">
    <defs>
      <linearGradient id="ringTeal" x1="0" y1="0" x2="1" y2="0">
        <stop offset="0" stop-color="#1c9fc7"/><stop offset="1" stop-color="#19b79a"/>
      </linearGradient>
      <linearGradient id="ringSea" x1="0" y1="0" x2="1" y2="0">
        <stop offset="0" stop-color="#17b3a0"/><stop offset="1" stop-color="#35b67d"/>
      </linearGradient>
      <linearGradient id="ringGreen" x1="0" y1="0" x2="1" y2="0">
        <stop offset="0" stop-color="#3db55a"/><stop offset="1" stop-color="#8cc63f"/>
      </linearGradient>
      <linearGradient id="ringLime" x1="0" y1="0" x2="1" y2="0">
        <stop offset="0" stop-color="#7dc242"/><stop offset="1" stop-color="#f2c318"/>
      </linearGradient>
    </defs>

    <rect class="frame-fill" width="1200" height="1062" fill="var(--magenta)"/>
    <path class="white-field" d="M0,0 H968 C1110,90 1210,330 1170,540 C1120,800 820,990 560,995 C350,1000 120,950 0,890 Z" fill="var(--white)"/>
    <path class="field-outline" d="M978,0 C1128,92 1222,330 1182,546 C1132,812 830,1006 560,1008 C350,1011 120,962 0,902" fill="none" stroke="#000" stroke-width="3"/>

    <!-- step icon rings -->
    <g class="icon step-1-icon">
      <path d="M82,390 A98,98 0 0 0 278,390" fill="none" stroke="url(#ringTeal)" stroke-width="9" stroke-linecap="round"/>
      <circle cx="180" cy="388" r="82" fill="var(--white)" stroke="var(--ring-grey)" stroke-width="10"/>
      <rect x="126" y="346" width="108" height="84" rx="8" fill="var(--scene-soft)" role="img" aria-label="Illustration of a dress shopping web page"/>
    </g>
    <g class="icon step-2-icon">
      <path d="M324,686 A98,98 0 0 1 520,686" fill="none" stroke="url(#ringSea)" stroke-width="9" stroke-linecap="round"/>
      <circle cx="422" cy="686" r="82" fill="var(--white)" stroke="var(--ring-grey)" stroke-width="10"/>
      <rect x="366" y="644" width="114" height="84" rx="8" fill="var(--scene-soft)" role="img" aria-label="Illustration of a woman customizing dresses on a web page"/>
    </g>
    <g class="icon step-3-icon">
      <path d="M568,390 A98,98 0 0 0 764,390" fill="none" stroke="url(#ringGreen)" stroke-width="9" stroke-linecap="round"/>
      <circle cx="666" cy="388" r="82" fill="var(--white)" stroke="var(--ring-grey)" stroke-width="10"/>
      <rect x="610" y="344" width="112" height="90" rx="8" fill="var(--scene-soft)" role="img" aria-label="Illustration of a client meeting a designer in front of a dress display"/>
    </g>
    <g class="icon step-4-icon">
      <path d="M812,686 A98,98 0 0 1 1008,686" fill="none" stroke="url(#ringLime)" stroke-width="9" stroke-linecap="round"/>
      <circle cx="910" cy="686" r="82" fill="var(--white)" stroke="var(--ring-grey)" stroke-width="10"/>
      <rect x="856" y="648" width="110" height="80" rx="8" fill="#f1ebe8" role="img" aria-label="Illustration of a tailor stitching and a courier delivering a parcel"/>
    </g>

    <!-- wave bands -->
    <path id="bandSelect" class="band" d="M56,560 Q185,664 314,560" fill="none" stroke="var(--band-purple)" stroke-width="54"/>
    <path id="bandCustom" class="band" d="M293,560 Q424,396 556,560" fill="none" stroke="var(--band-blue)" stroke-width="54"/>
    <path id="bandDesigner" class="band" d="M531,560 Q662,664 793,560" fill="none" stroke="var(--band-sea)" stroke-width="54"/>
    <path id="bandStitch" class="band" d="M768,560 Q900,396 1032,560" fill="none" stroke="var(--band-lime)" stroke-width="54"/>

    <path id="labelSelect" d="M56,568 Q185,672 314,568" fill="none"/>
    <path id="labelCustom" d="M293,568 Q424,404 556,568" fill="none"/>
    <path id="labelDesigner" d="M531,568 Q662,672 793,568" fill="none"/>
    <path id="labelStitch" d="M768,568 Q900,404 1032,568" fill="none"/>

    <text class="band-label"><textPath href="#labelSelect" startOffset="50%" text-anchor="middle">SELECT DRESS</textPath></text>
    <text class="band-label"><textPath href="#labelCustom" startOffset="50%" text-anchor="middle">CUSTOMIZATION</textPath></text>
    <text class="band-label"><textPath href="#labelDesigner" startOffset="50%" text-anchor="middle">DESIGNER CONSULTATION</textPath></text>
    <text class="band-label"><textPath href="#labelStitch" startOffset="50%" text-anchor="middle">STITCH AND DELIVER</textPath></text>
  </svg>

  <h1 class="title">HOW IT WORKS</h1>

  <section class="step step-1">
    <h2 class="step-label">STEP <span class="num">01</span></h2>
    <p class="step-text">Its time to choose the beauty you<br>want to adorn yourself with. We<br>have a wide collection of premium<br>dresses, colours and accessories.<br>There is something for everyone!<br>All you need to do is pick. If you<br>can’t find what you are looking for<br>then you can share a picture of<br>what you want, we will get it done<br>whatever you want.</p>
  </section>

  <section class="step step-2">
    <h2 class="step-label">STEP <span class="num">02</span></h2>
    <p class="step-text">Everyone is different; hence we<br>realise the need for customization<br>of the design and size. Here you<br>select exactly how you want your<br>dress to be. From sleeves to cuts,<br>everything will be done as per your<br>wish. Enter your measurements, lo<br>and behold! You’re done. Leave<br>your comments for even more<br>customization.</p>
  </section>

  <section class="step step-3">
    <h2 class="step-label">STEP <span class="num">03</span></h2>
    <p class="step-text">We as a user-friendly brand, aspire<br>to provide the best of services to<br>our clients. Our expert lady<br>designers will help you for<br>everything right from selecting of<br>fabric to design of dress to<br>necessary accessories. Our<br>designers are just a call away!</p>
  </section>

  <section class="step step-4">
    <h2 class="step-label">STEP <span class="num">04</span></h2>
    <p class="step-text">After you have placed your<br>order, we confirm and verify the<br>details. The boutique<br>completes your order, sends it<br>to us and we deliver it to your<br>doorstep. We also have a team<br>of designers in-house to cater<br>to your premium dressing<br>needs.</p>
  </section>

  <p class="web-address">www.VelmoraStyles.com</p>
</main>
</body>
</html>
```